IT Network Consultancy - Brochure

m2 relays is a IT network consultancy based in London. We're looking for a smart, modern and professional brochure in A4 format. Our website is here: www.m2relays.co.uk. We likely will require the brochure in two formats:

PDF / Scroll Down (The most common distribution of the brochure will be PDF, which will scroll down page after page):

Page 1 - Front page
Page 2 - Portrait / scroll down
Page 3 - Portrait / scroll down
Page 4 - Portrait / scroll down
Page 5 - Portrait / scroll down
Page 6 - Back page

Side by Side / Professionally Printed:

Page 1 - Front page
Page 2/3 - Side by side
Page 4/5 - Side by side
Page 6 - Back page
Updates

Please note - I made a number of changes to the design brief after initially submitting it.

I have also increased the first prize budget from £150 to £200 (US $327)

Images may be used - no pictures of people though or anything too bright...

Reason: We're extending the deadline as we haven't received as many designs as we'd liked (one so far!)

Following a question from another designer:

We're a technology consultancy, not a technology company.  We don't need any futuristic graphics, just something that looks clean and professional.  Almost along the lines of financial services but not to traditional.

Target Market(s)

Large enterprise / global companies / corporates

Industry/Entity Type

Distribution

Requirements
Must have
• Incorporate our logo - which is attached to the project. They are in AI format (can be opened in Inkscape).

Initially the brochure is to be used specifically for our company profile / fact sheet (see attached PPT for text).

We would like to have a template we can also use for future documents.

Fonts should be simple.
Nice to have
• The project does not have to conform to the colour of our website but this should give you inspiration of the style we like.

A way to incorporate the design into MS PowerPoint, i.e. a template for corporate presentations.
Should not have
• Bright colours.

```html
<!DOCTYPE html>
<html lang="en">
<head>
<meta charset="utf-8">
<title>m2 relays – Engagement &amp; Delivery Process</title>
<link rel="stylesheet" href="https://fonts.googleapis.com/css2?family=Open+Sans:wght@400;600;700;800&display=swap">
<style>
  :root{
    --backdrop:#cbcbcb;
    --paper:#ffffff;
    --slate:#323c44;
    --slate-light:#4a555e;
    --mist:#9aa3aa;
    --copy-light:#c4cace;
    --title:#2f3a42;
    --ring:#d6dadc;
  }
  *{box-sizing:border-box;margin:0;padding:0}
  html,body{width:1200px;height:900px;overflow:hidden}
  body{background:var(--backdrop);font-family:"Open Sans",Arial,sans-serif;position:relative}
  .page{position:absolute;left:302px;top:25px;width:601px;height:850px;background:var(--paper);overflow:hidden}

  .masthead{position:absolute;left:0;top:0;width:601px;height:105px;background:var(--slate);overflow:hidden}
  .masthead-sheen{position:absolute;inset:0}
  .masthead-rule{position:absolute;left:40px;right:20px;top:96px;height:2px;
    background:linear-gradient(90deg,transparent,#9aa3aa 40%,#e8ebec 75%,transparent)}
  .brand{position:absolute;right:34px;top:64px;display:flex;align-items:center;gap:7px;
    color:#e6e9eb;font-size:15px;font-weight:600;letter-spacing:1.5px;text-transform:uppercase}
  .brand-dot{width:12px;height:12px;border-radius:50%;background:#e6e9eb}

  .title-tab{position:absolute;left:0;top:127px;width:61px;height:31px;background:var(--slate);border-radius:0 16px 16px 0}
  .title-tab::after{content:"";position:absolute;right:4px;top:4px;width:23px;height:23px;border-radius:50%;
    background:var(--slate-light);border:3px solid #e6e9eb}
  .page-title{position:absolute;left:93px;top:128px;font-size:20px;font-weight:800;color:var(--title);letter-spacing:.2px}
  .page-intro{position:absolute;left:93px;top:166px;font-size:9px;color:#333}

  .stage{position:absolute;left:0;width:601px;height:95px}
  .stage-card{position:absolute;left:103px;top:0;width:438px;height:95px;background:var(--slate);border-radius:5px}
  .stage-pointer{position:absolute;left:120px;top:29px;width:55px;height:38px;background:var(--paper);
    clip-path:polygon(0 0,100% 50%,0 100%)}
  .stage-badge{position:absolute;left:47px;top:0;width:96px;height:96px;border-radius:50%;background:var(--paper);
    border:8px solid var(--slate);display:flex;align-items:center;justify-content:center;text-align:center;
    font-size:10px;font-weight:700;color:var(--title);line-height:1.25}
  .stage-notes{position:absolute;left:188px;font-size:8px;line-height:12.8px;color:var(--copy-light);list-style:none}
  .stage-notes .sub{padding-left:18px}
  .stage-notes .indent{padding-left:9px}
  .stage-number{position:absolute;left:514px;top:28px;font-size:30px;font-weight:700;color:#fff}

  .flow{position:absolute;left:0;top:0;width:601px;height:850px;pointer-events:none}

  .change-band{position:absolute;left:0;top:721px;width:601px;height:57px;background:var(--mist)}
  .change-note{position:absolute;left:188px;top:22px;font-size:8px;color:#2a3036}
  .change-pointer{position:absolute;left:490px;top:18px;width:22px;height:20px;background:var(--paper);
    clip-path:polygon(0 50%,100% 0,100% 100%)}
  .change-badge{position:absolute;left:508px;top:0;width:57px;height:57px;border-radius:50%;background:var(--slate);
    border:4px solid var(--ring);display:flex;align-items:center;justify-content:center;text-align:center;
    color:#fff;font-size:6px;font-weight:700;line-height:1.3}

  .footer{position:absolute;left:0;top:790px;width:601px;height:60px;
    background:linear-gradient(180deg,#6d767d 0%,var(--slate) 45%,var(--slate) 100%)}
  .footer-contact{position:absolute;left:85px;top:25px;font-size:7px;color:#d8dcdf;white-space:nowrap}
  .footer-contact span::before{content:"";display:inline-block;width:0;height:0;border-left:5px solid #d8dcdf;
    border-top:3px solid transparent;border-bottom:3px solid transparent;margin-right:2px}
  .footer-web{position:absolute;right:34px;top:21px;font-size:11px;font-weight:700;color:#fff;letter-spacing:.3px}
</style>
</head>
<body>
<main class="page">
  <header class="masthead">
    <svg class="masthead-sheen" width="601" height="105" viewBox="0 0 601 105" aria-hidden="true">
      <defs>
        <linearGradient id="sheen" x1="0" y1="0" x2="1" y2="0">
          <stop offset="0" stop-color="#55606a" stop-opacity="0"/>
          <stop offset=".6" stop-color="#5d6872" stop-opacity=".8"/>
          <stop offset="1" stop-color="#3a444c" stop-opacity=".4"/>
        </linearGradient>
      </defs>
      <polygon points="170,0 601,0 601,70" fill="url(#sheen)"/>
    </svg>
    <div class="masthead-rule"></div>
    <div class="brand"><span class="brand-dot"></span>m2 relays</div>
  </header>

  <div class="title-tab"></div>
  <h1 class="page-title">ENGAGEMENT &amp; DELIVERY PROCESS</h1>
  <p class="page-intro">A typical engagement process</p>

  <section class="stage" style="top:193px">
    <div class="stage-card"></div>
    <div class="stage-pointer"></div>
    <div class="stage-badge">Engagement</div>
    <ul class="stage-notes" style="top:4px">
      <li>1. Project initiation meeting</li>
      <li>2. Key factors to determine:</li>
      <li class="sub">• Size</li>
      <li class="sub">• Scope</li>
      <li class="sub">• Requirements</li>
      <li class="sub">• Timing</li>
      <li class="sub">• Budget</li>
    </ul>
    <div class="stage-number">1</div>
  </section>

  <section class="stage" style="top:298px">
    <div class="stage-card"></div>
    <div class="stage-pointer"></div>
    <div class="stage-badge">Scope</div>
    <ul class="stage-notes" style="top:27px">
      <li>1. Project Scope of Work document produced and</li>
      <li class="indent">presented to Engagement Manager</li>
      <li>2. Accepted and signed by Engagement Manager</li>
    </ul>
    <div class="stage-number">2</div>
  </section>

  <section class="stage" style="top:404px">
    <div class="stage-card"></div>
    <div class="stage-pointer"></div>
    <div class="stage-badge">Delivery</div>
    <ul class="stage-notes" style="top:14px">
      <li>1. Project initiated</li>
      <li>2. Delivery staff agreed and vetted by customer</li>
      <li>3. Delivery executed</li>
      <li>4. If requested the project change management cycle</li>
      <li class="indent">can be initiated and the scope changed</li>
    </ul>
    <div class="stage-number">3</div>
  </section>

  <section class="stage" style="top:509px">
    <div class="stage-card"></div>
    <div class="stage-pointer"></div>
    <div class="stage-badge">Completion</div>
    <ul class="stage-notes" style="top:15px">
      <li>1. Delivery submitted</li>
      <li>2. Peer &nbsp;/ management review and revision</li>
      <li>3. Project / Engagement Manager acceptance and signoff</li>
      <li>4. Technical, design and support documentation completed and handover</li>
    </ul>
    <div class="stage-number">4</div>
  </section>

  <section class="stage" style="top:615px">
    <div class="stage-card"></div>
    <div class="stage-pointer"></div>
    <div class="stage-badge">Support &amp;<br>Mainatance</div>
    <ul class="stage-notes" style="top:41px">
      <li>Follow up support after project closure</li>
    </ul>
    <div class="stage-number">5</div>
  </section>

  <svg class="flow" viewBox="0 0 601 850" aria-hidden="true">
    <defs>
      <marker id="head" markerWidth="8" markerHeight="8" refX="6" refY="4" orient="auto">
        <path d="M0,0 L8,4 L0,8 Z" fill="#323c44"/>
      </marker>
      <marker id="head-dot" markerWidth="7" markerHeight="7" refX="5" refY="3.5" orient="auto">
        <path d="M0,0 L7,3.5 L0,7 Z" fill="#8a9399"/>
      </marker>
    </defs>
    <g fill="none" stroke="#323c44" stroke-width="1.6" marker-end="url(#head)">
      <path d="M550 242 C 590 262, 588 312, 548 328"/>
      <path d="M550 348 C 590 368, 588 418, 548 434"/>
      <path d="M550 453 C 590 473, 588 523, 548 539"/>
      <path d="M550 558 C 590 578, 588 628, 548 644"/>
    </g>
    <path d="M36 532 C 18 505, 20 385, 46 360" fill="none" stroke="#8a9399" stroke-width="1.6"
          stroke-dasharray="2 2.5" marker-end="url(#head-dot)"/>
  </svg>

  <section class="change-band">
    <p class="change-note">Change to the scope can occur during the Delivery or Completion phases.</p>
    <div class="change-pointer"></div>
    <div class="change-badge">Change<br>Management</div>
  </section>

  <footer class="footer">
    <p class="footer-contact"><span></span>phone: +44 (0) 1632 960418 <span></span>mobile: +44 (0) 7700 900215 <span></span>email: info@m2relays.co.uk</p>
    <p class="footer-web">www.m2relays.co.uk</p>
  </footer>
</main>
</body>
</html>
```